Awesome Dessert Baker needs Sticker Design

My wife is an incredible baker. She specializes in desserts and everyone that tastes her baked goods has told her to start selling them. She recently decided to go into business and just through word of mouth and her reputation she is already getting steady orders.

She is looking to have a sticker developed to put on her cake boxes and packaging.

She wants the following:
1. Colors to be used- hot pink, purple, white
2. Want a sleek, modern design and style incorporating following:
name: Whisked by Nola
tel: 917 382 6140
email: nola@whiskedbynola.example

**no old fashion baking references like rolling pins, aprons, ect.

We want the sticker to be very appealing and eye catching that will further promote her image and business.

Industry/Entity Type

Fashion

Requirements
Must have
• Must contain the following information:

Whisked by Nola
917 382 6140 (please make small and discreet)
nola@whiskedbynola.example (please make small and discreet)
Should not have
• **no old fashion baking references like rolling pins, aprons, ect.

```html
<!DOCTYPE html>
<html lang="en">
<head>
<meta charset="utf-8">
<title>Whisked by Nola — Sticker</title>
<link rel="stylesheet" href="https://fonts.googleapis.com/css2?family=Bree+Serif&display=swap">
<style>
  :root {
    --canvas: #ffffff;
    --sticker-edge: #cfcfcf;
    --hot-pink: #e3167f;
    --deep-pink: #c10c68;
    --blush: #fbd3e7;
    --white: #ffffff;
  }
  html, body {
    margin: 0;
    padding: 0;
    width: 1200px;
    height: 1155px;
    overflow: hidden;
    background: var(--canvas);
  }
  .sticker {
    display: block;
    width: 1200px;
    height: 1155px;
  }
  .sticker__cut { fill: var(--white); stroke: var(--sticker-edge); stroke-width: 2; }
  .sticker__rim { fill: var(--hot-pink); }
  .sticker__gap { fill: var(--blush); }
  .brand-name {
    font-family: "Bree Serif", Georgia, serif;
    font-weight: 400;
    font-size: 92px;
    fill: var(--white);
  }
  .contact {
    font-family: "Bree Serif", Georgia, serif;
    font-weight: 400;
    font-size: 31px;
    fill: var(--white);
  }
</style>
</head>
<body>
<svg class="sticker" viewBox="0 0 1200 1155" xmlns="http://www.w3.org/2000/svg">
  <defs>
    <radialGradient id="panel-glow" cx="50%" cy="45%" r="60%">
      <stop offset="0%" stop-color="#f04a9c"/>
      <stop offset="60%" stop-color="#e3167f"/>
      <stop offset="100%" stop-color="#c10c68"/>
    </radialGradient>
  </defs>

  <ellipse class="sticker__cut" cx="600" cy="577" rx="505" ry="412"/>

  <ellipse class="sticker__rim" cx="600" cy="577" rx="478" ry="385"
           role="img" aria-label="Border of glossy pink beads around the sticker"/>
  <ellipse class="sticker__gap" cx="600" cy="577" rx="440" ry="350"/>

  <ellipse cx="600" cy="577" rx="425" ry="336" fill="url(#panel-glow)"
           role="img" aria-label="Hot pink sunburst background with soft floating bubbles"/>

  <text class="brand-name" x="600" y="560" text-anchor="middle">Whisked by Nola</text>

  <text class="contact" x="600" y="790" text-anchor="middle">nola@whiskedbynola.example</text>
  <text class="contact" x="600" y="838" text-anchor="middle">917 382 6140</text>
</svg>
</body>
</html>
```